Business card design needed

I need a business card for my private practice. I would like to see the designs that use bright blue and white. I would like to see similar designs as to the card below:
http://blog.printvarno.com/2009/designing-a-business-card-with-pv-ks517-template.html
I would like to see the back of the card have room for appointment times. Thank you.

Industry/Entity Type
Business
Contact Information for Business Card
Brightwater Counselling & Wellness Services
Helen Dorsey B.Psychology
Registered Psychologist
Building C, Level 3, 14 Marrow Crescent, Canberra, ACT 2601
T: (02) 6287 5912
F: (02) 6287 5930
info@brightwatercounselling.com.au
www.brightwatercounselling.com.au

```html
<!DOCTYPE html>
<html lang="en">
<head>
<meta charset="UTF-8">
<title>Brightwater Counselling &amp; Wellness Services – Business Card</title>
<link rel="stylesheet" href="https://fonts.googleapis.com/css2?family=Questrial&display=swap">
<style>
  :root {
    --brand-blue: #12bde6;
    --brand-blue-light: #2fd0f2;
    --brand-blue-deep: #0aa3d1;
    --card-white: #ffffff;
    --card-grey: #8a8f94;
    --rule-grey: #c9d3d8;
    --text-blue: #1aa9d6;
    --stage: #eef1f3;
  }
  * { box-sizing: border-box; margin: 0; padding: 0; }
  html, body {
    width: 1200px;
    height: 1000px;
    overflow: hidden;
    background: var(--stage);
    font-family: "Questrial", "Century Gothic", sans-serif;
  }
  .sheet {
    width: 1200px;
    height: 1000px;
    display: flex;
    flex-direction: column;
    align-items: center;
    justify-content: center;
    gap: 60px;
  }
  .card {
    width: 700px;
    height: 400px;
    position: relative;
    box-shadow: 0 8px 24px rgba(0, 0, 0, 0.12);
    overflow: hidden;
  }

  /* Front */
  .card--front {
    background: linear-gradient(150deg, var(--brand-blue-light) 0%, var(--brand-blue) 55%, var(--brand-blue-deep) 100%);
    color: var(--card-white);
  }
  .front-identity {
    position: absolute;
    left: 60px;
    bottom: 80px;
    display: flex;
    align-items: center;
    gap: 24px;
  }
  .front-identity__mark {
    width: 96px;
    height: 96px;
    border-radius: 50%;
    background: var(--card-white);
    flex: none;
  }
  .front-identity__name {
    font-size: 25px;
    white-space: nowrap;
  }
  .front-identity__web {
    font-size: 13px;
    margin-top: 6px;
    opacity: 0.9;
  }

  /* Back */
  .card--back {
    background: var(--card-white);
  }
  .back-details {
    position: absolute;
    right: 50px;
    top: 50px;
    text-align: right;
  }
  .back-details__company {
    font-size: 24px;
    color: var(--text-blue);
    white-space: nowrap;
  }
  .back-details__web {
    font-size: 13px;
    color: var(--card-grey);
    margin-top: 6px;
  }
  .back-contact {
    position: absolute;
    right: 50px;
    bottom: 44px;
    text-align: right;
    color: var(--text-blue);
    font-size: 13px;
    line-height: 1.6;
  }
  .back-contact__person {
    font-size: 17px;
    margin-bottom: 2px;
  }
  .back-contact__role {
    color: var(--card-grey);
    margin-bottom: 8px;
  }
  .appointments {
    position: absolute;
    left: 50px;
    bottom: 44px;
    width: 270px;
  }
  .appointments__title {
    font-size: 14px;
    color: var(--text-blue);
    margin-bottom: 10px;
  }
  .appointments__row {
    display: flex;
    gap: 14px;
    margin-top: 14px;
    font-size: 11px;
    color: var(--card-grey);
  }
  .appointments__field {
    flex: 1;
    border-bottom: 1px solid var(--rule-grey);
    padding-bottom: 3px;
  }
</style>
</head>
<body>
  <main class="sheet">
    <section class="card card--front" aria-label="Card front">
      <div class="front-identity">
        <span class="front-identity__mark"></span>
        <div>
          <p class="front-identity__name">Brightwater Counselling &amp; Wellness Services</p>
          <p class="front-identity__web">www.brightwatercounselling.com.au</p>
        </div>
      </div>
    </section>

    <section class="card card--back" aria-label="Card back">
      <div class="back-details">
        <p class="back-details__company">Brightwater Counselling &amp; Wellness Services</p>
        <p class="back-details__web">www.brightwatercounselling.com.au</p>
      </div>

      <div class="appointments">
        <p class="appointments__title">Your next appointment</p>
        <div class="appointments__row">
          <span class="appointments__field">Date</span>
          <span class="appointments__field">Time</span>
        </div>
        <div class="appointments__row">
          <span class="appointments__field">Date</span>
          <span class="appointments__field">Time</span>
        </div>
        <div class="appointments__row">
          <span class="appointments__field">Date</span>
          <span class="appointments__field">Time</span>
        </div>
      </div>

      <div class="back-contact">
        <p class="back-contact__person">Helen Dorsey B.Psychology</p>
        <p class="back-contact__role">Registered Psychologist</p>
        <p>Building C, Level 3, 14 Marrow Crescent,</p>
        <p>Canberra, ACT 2601</p>
        <p>T: (02) 6287 5912 &nbsp; F: (02) 6287 5930</p>
        <p>info@brightwatercounselling.com.au</p>
      </div>
    </section>
  </main>
</body>
</html>
```